Health and Wellness Company Business Card

I need a business card design that is clean and uses modern minimalist style. The design should incorporate our logo (see attached). I would also like to use embossing on the cards so that they also have a great feel. I am open to the card using one or more colors, and these do not have to correspond to the colors in the concept paper. The card can either be one-sided or use both sides of the card.The logo uses the Avenir font.

I will need the file designed in Adobe CS and compatible with CS5.5 (Illustrator preferable) and I'll need the working file (for example: .ai) once the project is complete so that I can change the names/contact info/etc for each variation of the card.

This needs to be a memorable card for the recipient. They should think: "This is a great business card" either because of its simplicity or embossing effects or use of color.

Target Market(s)

The audience for our company has two main groups: people who pay for healthcare (insurers, companies, researcher companies) and people with chronic health conditions who are the consumers of our services and resources.

Industry/Entity Type

Business

Requirements
Must have
• Essential components of the card include: Company logo, contact Name (Mark Tolley), phone number (5808127346), email address (mtolley@brenquora.com), slogan/tagline that consists of ~30-40 characters (Use Lorem Ipsum)
Nice to have
• These fall just slightly short of "must have" to allow for design flexibility: Embossing or spot varnish effects and a splash of color
Should not have
• Designs with these components will not be successful: flashy or showy designs that are not professional in appearance, and lots of different colors

```html
<!DOCTYPE html>
<html lang="en">
<head>
<meta charset="utf-8">
<title>Brenquora Business Card</title>
<link rel="stylesheet" href="https://fonts.googleapis.com/css2?family=Mulish:ital,wght@0,300;0,400;1,300&display=swap">
<style>
  :root {
    --backdrop: #d9d8de;
    --card: #e9e8ee;
    --card-shade: #dedde6;
    --ink: #6b6f8c;
    --ink-strong: #5a6196;
    --band-dark: #6b78a2;
    --band-light: #aab1cd;
    --stripe: #c5cae0;
  }
  * { margin: 0; padding: 0; box-sizing: border-box; }
  html, body {
    width: 1200px;
    height: 900px;
    overflow: hidden;
    background: var(--backdrop);
    font-family: "Mulish", "Avenir", sans-serif;
  }
  .business-card {
    position: absolute;
    left: 75px;
    top: 150px;
    width: 1050px;
    height: 600px;
    background: linear-gradient(160deg, #f1f0f5 0%, var(--card) 55%, var(--card-shade) 100%);
    box-shadow: 0 12px 30px rgba(40, 40, 60, 0.18);
    overflow: hidden;
  }
  .brand {
    position: absolute;
    left: 150px;
    top: 150px;
    display: flex;
    align-items: center;
    gap: 22px;
  }
  .brand-square {
    width: 34px;
    height: 34px;
    background: var(--ink);
    border-radius: 5px;
  }
  .brand-name {
    font-size: 44px;
    font-weight: 400;
    letter-spacing: 0.42em;
    text-transform: uppercase;
    color: var(--ink);
  }
  .contact {
    position: absolute;
    left: 640px;
    top: 265px;
    color: var(--ink);
  }
  .contact-name {
    font-size: 34px;
    font-weight: 300;
    color: var(--ink-strong);
    letter-spacing: 0.04em;
    margin-bottom: 26px;
  }
  .contact-line {
    font-size: 21px;
    font-weight: 300;
    line-height: 1.35;
    letter-spacing: 0.03em;
  }
  .tagline {
    position: absolute;
    left: 60px;
    top: 440px;
    font-size: 21px;
    font-style: italic;
    font-weight: 300;
    letter-spacing: 0.03em;
    color: var(--ink);
  }
  .accent-band {
    position: absolute;
    left: 0;
    bottom: 0;
    width: 100%;
    height: 105px;
  }
</style>
</head>
<body>
  <main class="business-card">
    <div class="brand">
      <span class="brand-square"></span>
      <span class="brand-name">brenquora</span>
    </div>

    <div class="contact">
      <p class="contact-name">Mark Tolley</p>
      <p class="contact-line">5808127346</p>
      <p class="contact-line">mtolley@brenquora.com</p>
    </div>

    <p class="tagline">Lorem Ipsum is simply dummy text of the printing and typesetting industry.</p>

    <svg class="accent-band" viewBox="0 0 1050 105" preserveAspectRatio="none" aria-hidden="true">
      <defs>
        <linearGradient id="band-fill" x1="0" y1="0" x2="1" y2="0">
          <stop offset="0" stop-color="var(--band-dark)"/>
          <stop offset="1" stop-color="var(--band-light)"/>
        </linearGradient>
      </defs>
      <rect width="1050" height="105" fill="url(#band-fill)"/>
      <polygon points="330,0 345,0 320,105 305,105" fill="var(--stripe)" opacity="0.75"/>
      <polygon points="360,0 395,0 370,105 335,105" fill="var(--band-dark)"/>
      <polygon points="410,0 422,0 397,105 385,105" fill="var(--stripe)" opacity="0.75"/>
    </svg>
  </main>
</body>
</html>
```